PACKAGING DESIGN NEEDED - TEMPLATE SUPPLIED - UPDATED BRAND MEADOW

Our company needs submissions for an outer box similar to a cereal box which will house sachets of instant Yoghurt Mix

I have attached a template for the core design and the correct varietals and nutrition info can be inserted later

We need 2 boxes

1- Natural Greek Yoghurt x 4 Sachets

2- Natural Greek Yoghurt with Honey x 2 Sachets and Boysenberry Yoghurt x 2 Sachets

I am initially looking for a design concept and the finer details can be inserted later

Our contract manufacturer has a website that may assist with preliminary ideas and you can see the sachets but not the boxes. We will not be printing sachets so we focus on the box but the website will assist.

http://www.corvellidairy.example/au/

I have also attached some shots of the companies other brand which features and animated cow so it can again synch you with their style.

The Brand is now MEADOW and another logo can be created with this name for the excercise....Animated cow could be used or similar

Thanks
Tomas

Target Market(s)

China

Industry/Entity Type

It Company

Font styles to use
Sans Serif

Requirements
Must have
• Clean and Fresh looking

```html
<!DOCTYPE html>
<html lang="en">
<head>
<meta charset="utf-8">
<title>Meadow Yoghurt Carton Concepts</title>
<link rel="stylesheet" href="https://fonts.googleapis.com/css2?family=Varela+Round&family=Noto+Serif+SC:wght@500&family=Cutive+Mono&family=Arimo:wght@400;700&display=swap">
<style>
  :root {
    --page: #ffffff;
    --tan-light: #d8b98c;
    --tan-mid: #c4a57a;
    --tan-front: #b48f5c;
    --tan-back: #a88a64;
    --ink-brown: #3b2f22;
    --charcoal: #1e2320;
    --charcoal-back: #252a27;
    --slate: #9eaec0;
    --slate-dark: #8797a9;
    --logo-plate: #9a9a9a;
    --teal-ink: #5f8b90;
    --studio: #d8d8d8;
    --blueprint: #4aa3cd;
    --sheet: #ffffff;
    --sheet-tint: #c8d8e4;
    --edge: #2a2a2a;
  }
  html, body { margin: 0; padding: 0; overflow: hidden; background: var(--page); }
  .board { display: block; width: 1200px; height: 800px; }
  .logo-word { font-family: "Varela Round", sans-serif; fill: #ffffff; }
  .product-title { font-family: "Varela Round", sans-serif; fill: #ffffff; }
  .claim { font-family: "Cutive Mono", monospace; fill: #f4ead8; }
  .hanzi { font-family: "Noto Serif SC", serif; fill: var(--ink-brown); }
  .hanzi-caption { font-family: "Cutive Mono", monospace; fill: var(--ink-brown); }
  .hanzi-teal { font-family: "Noto Serif SC", serif; fill: var(--teal-ink); }
  .nf-title { font-family: "Arimo", sans-serif; font-weight: 700; fill: #000; }
  .nf-row { font-family: "Arimo", sans-serif; fill: #000; }
  .cut { stroke: var(--edge); stroke-width: 0.5; }
</style>
</head>
<body>
<svg class="board" viewBox="0 0 900 600" xmlns="http://www.w3.org/2000/svg">
  <defs>
    <linearGradient id="splash-tones" x1="0" y1="0" x2="0" y2="1">
      <stop offset="0" stop-color="#b48f5c"/>
      <stop offset="0.5" stop-color="#efe8dc"/>
      <stop offset="1" stop-color="#b48f5c"/>
    </linearGradient>
    <radialGradient id="bowl-tones">
      <stop offset="0" stop-color="#f2f4f2"/>
      <stop offset="1" stop-color="#6f9ea4"/>
    </radialGradient>
    <radialGradient id="swirl-tones">
      <stop offset="0" stop-color="#3a423e"/>
      <stop offset="1" stop-color="#1e2320"/>
    </radialGradient>
    <g id="nutrition-panel">
      <rect x="0" y="0" width="67" height="140" fill="#fff" stroke="#000" stroke-width="0.6"/>
      <text class="nf-title" x="3" y="11" font-size="8.5">Nutrition Facts</text>
      <line x1="3" y1="14" x2="64" y2="14" stroke="#000" stroke-width="1.5"/>
      <text class="nf-row" x="3" y="21" font-size="3.6">Serving Size 1 sachet</text>
      <text class="nf-row" x="3" y="26" font-size="3.6">Servings 4</text>
      <line x1="3" y1="29" x2="64" y2="29" stroke="#000" stroke-width="1.2"/>
      <text class="nf-row" x="3" y="35" font-size="3.6">Calories 120</text>
      <line x1="3" y1="38" x2="64" y2="38" stroke="#000" stroke-width="0.4"/>
      <text class="nf-row" x="3" y="44" font-size="3.6">Total Fat 3g</text>
      <line x1="3" y1="47" x2="64" y2="47" stroke="#000" stroke-width="0.3"/>
      <text class="nf-row" x="3" y="53" font-size="3.6">Sodium 60mg</text>
      <line x1="3" y1="56" x2="64" y2="56" stroke="#000" stroke-width="0.3"/>
      <text class="nf-row" x="3" y="62" font-size="3.6">Carbohydrate 18g</text>
      <line x1="3" y1="65" x2="64" y2="65" stroke="#000" stroke-width="0.3"/>
      <text class="nf-row" x="3" y="71" font-size="3.6">Protein 6g</text>
      <line x1="3" y1="74" x2="64" y2="74" stroke="#000" stroke-width="1.2"/>
      <text class="nf-row" x="3" y="81" font-size="3.6">Calcium 20%</text>
      <line x1="3" y1="84" x2="64" y2="84" stroke="#000" stroke-width="0.3"/>
      <text class="nf-row" x="3" y="90" font-size="3.6">Vitamin A 2%</text>
      <line x1="3" y1="93" x2="64" y2="93" stroke="#000" stroke-width="0.3"/>
      <text class="nf-row" x="3" y="104" font-size="3.2">Ingredients listed on pack</text>
      <line x1="3" y1="108" x2="64" y2="108" stroke="#000" stroke-width="0.3"/>
      <line x1="3" y1="118" x2="64" y2="118" stroke="#000" stroke-width="0.3"/>
      <line x1="3" y1="128" x2="64" y2="128" stroke="#000" stroke-width="0.3"/>
    </g>
  </defs>

  <!-- Carton A: boysenberry, warm kraft -->
  <g class="carton carton-kraft">
    <polygon class="cut" points="40,75 44,60 64,60 70,75" fill="var(--tan-light)"/>
    <polygon class="cut" points="35,255 70,255 70,275 62,287 40,287 35,275" fill="var(--tan-light)"/>
    <rect class="cut" x="35" y="75" width="35" height="180" fill="var(--tan-light)"/>
    <text class="hanzi" x="52" y="132" font-size="20" text-anchor="middle">健</text>
    <text class="hanzi-caption" x="52" y="144" font-size="6" text-anchor="middle">Health</text>
    <text class="hanzi" x="52" y="172" font-size="20" text-anchor="middle">漢</text>
    <text class="hanzi-caption" x="52" y="186" font-size="6" text-anchor="middle">Health</text>
    <text class="hanzi" x="52" y="214" font-size="20" text-anchor="middle">幸</text>
    <text class="hanzi-caption" x="52" y="230" font-size="6" text-anchor="middle">Happiness</text>

    <rect class="cut" x="70" y="75" width="128" height="20" fill="var(--tan-light)"/>
    <rect class="cut" x="70" y="95" width="128" height="160" fill="var(--tan-front)"/>
    <rect class="cut" x="70" y="255" width="128" height="20" fill="var(--tan-mid)"/>
    <line x1="90" y1="268" x2="180" y2="268" stroke="var(--edge)" stroke-width="1.4"/>
    <rect x="104" y="103" width="44" height="19" fill="var(--logo-plate)"/>
    <text class="logo-word" x="126" y="116.5" font-size="10" text-anchor="middle">Meadow</text>
    <rect x="105" y="122" width="80" height="115" fill="url(#splash-tones)" role="img" aria-label="Creamy yoghurt splash with boysenberries and leaves"/>
    <text class="product-title" x="134" y="149" font-size="11.5" text-anchor="middle">Boysenberry Yoghurt</text>

    <polygon class="cut" points="198,75 203,60 228,60 233,75" fill="var(--tan-light)"/>
    <polygon class="cut" points="198,255 233,255 233,270 226,276 205,276 198,270" fill="var(--tan-light)"/>
    <rect class="cut" x="198" y="75" width="35" height="180" fill="var(--tan-light)"/>
    <text class="claim" font-size="8.5" text-anchor="middle">
      <tspan x="216" y="130">"yogurt"</tspan>
      <tspan x="216" y="143">-</tspan>
      <tspan x="216" y="156">smoothe</tspan>
      <tspan x="216" y="168">skin</tspan>
      <tspan x="216" y="180">and</tspan>
      <tspan x="216" y="192">soothes</tspan>
      <tspan x="216" y="204">the</tspan>
      <tspan x="216" y="216">stomach</tspan>
    </text>

    <path class="cut" d="M233,70 L233,58 Q233,50 241,50 L352,50 Q360,50 360,58 L360,70 Z" fill="var(--tan-back)"/>
    <rect class="cut" x="233" y="70" width="127" height="185" fill="var(--tan-back)"/>
    <rect class="cut" x="240" y="255" width="113" height="18" fill="var(--tan-back)"/>
    <use href="#nutrition-panel" x="289" y="105"/>
  </g>

  <!-- Carton B: natural, charcoal and slate -->
  <g class="carton carton-charcoal">
    <polygon class="cut" points="40,325 44,310 64,310 70,325" fill="var(--slate)"/>
    <polygon class="cut" points="35,505 70,505 70,522 62,530 40,530 35,522" fill="var(--slate)"/>
    <rect class="cut" x="35" y="325" width="35" height="180" fill="var(--slate)"/>

    <rect class="cut" x="70" y="325" width="128" height="20" fill="var(--slate)"/>
    <rect class="cut" x="70" y="345" width="128" height="160" fill="var(--charcoal)"/>
    <rect class="cut" x="70" y="505" width="128" height="20" fill="var(--charcoal)"/>
    <line x1="90" y1="517" x2="180" y2="517" stroke="#6b6b6b" stroke-width="1.4"/>
    <rect x="72" y="380" width="62" height="92" fill="url(#swirl-tones)" role="img" aria-label="Faint balance swirl decoration"/>
    <rect x="106" y="353" width="40" height="19" fill="var(--logo-plate)"/>
    <text class="logo-word" x="126" y="366.5" font-size="10" text-anchor="middle">Meadow</text>
    <rect x="100" y="412" width="50" height="38" fill="url(#bowl-tones)" role="img" aria-label="Bowl of natural Greek yoghurt"/>
    <text class="hanzi-teal" x="134" y="462" font-size="7" text-anchor="middle" letter-spacing="3">s u f</text>
    <text class="hanzi-teal" x="78" y="490" font-size="21">健 漢 幸</text>

    <polygon class="cut" points="198,325 203,310 228,310 233,325" fill="var(--slate)"/>
    <polygon class="cut" points="198,505 233,505 233,520 226,526 205,526 198,520" fill="var(--slate)"/>
    <rect class="cut" x="198" y="325" width="35" height="180" fill="var(--slate)"/>

    <path class="cut" d="M233,320 L233,308 Q233,300 241,300 L352,300 Q360,300 360,308 L360,320 Z" fill="var(--charcoal-back)"/>
    <rect class="cut" x="233" y="320" width="127" height="185" fill="var(--charcoal-back)"/>
    <rect class="cut" x="240" y="505" width="113" height="20" fill="var(--charcoal-back)"/>
    <use href="#nutrition-panel" x="284" y="353"/>
  </g>

  <!-- Template views -->
  <g class="template-views">
    <rect x="400" y="0" width="360" height="228" fill="var(--studio)" role="img" aria-label="Three-quarter renders of the carton template at three sizes"/>
    <rect x="400" y="228" width="360" height="372" fill="var(--blueprint)"/>
    <line x1="400" y1="338" x2="760" y2="338" stroke="#6fb6d8" stroke-width="0.6"/>
    <line x1="578" y1="228" x2="578" y2="338" stroke="#6fb6d8" stroke-width="0.6"/>
    <rect class="cut" x="448" y="246" width="72" height="84" fill="var(--sheet)"/>
    <rect class="cut" x="622" y="234" width="90" height="102" fill="var(--sheet-tint)"/>
    <polygon class="cut" points="450,425 712,425 698,445 698,510 464,510 464,445" fill="var(--sheet)"/>
    <polygon points="450,425 712,425 698,445 464,445" fill="var(--sheet-tint)"/>
    <rect class="cut" x="488" y="468" width="178" height="8" fill="var(--sheet-tint)"/>

    <rect x="778" y="0" width="102" height="600" fill="var(--blueprint)"/>
    <rect class="cut" x="797" y="12" width="65" height="270" fill="var(--sheet-tint)" stroke-width="1"/>
    <rect class="cut" x="797" y="300" width="65" height="290" fill="var(--sheet)" stroke-width="1"/>
  </g>
</svg>
</body>
</html>
```